Design a helpdesk ticketing platform *

We are launching a helpdesk ticketing platform. Very much like lumidesk.example, brightowl.example, calmhub.example, tidyqueue.example etc. We have a full mid-fidelity prototype built and we want someone to build the full fidelity of the product.

You can view the full mid-fidelity prototype here: https://shortlink.example/Qw8pLk

The best way moving forward is to just design the following 4 pages

- Main Dashboard https://shortlink.example/48vRxN
- All tickets https://shortlink.example/jbdYsW
- Viewing a ticket https://shortlink.example/mHqLtB
- Contacts https://shortlink.example/yKeoPd

Target Market(s)

Small business owners

Industry/Entity Type

Saas

Number of Pages Required

4 page

Font styles to use
Serif
Sans Serif

Colors

Designer to choose colors to be used in the design.

Requirements
Must have
• Must follow the prototype exactly. We are not looking for any UX changes. We want the designe xactly as the prototype is. We are only looking for design ideas.
Should not have
• modern, clean. We'd love to see the primary color as yellow, purple, orange, green or blue. You choose which one you think looks best and go with that.

```html
<!DOCTYPE html>
<html lang="en">
<head>
<meta charset="utf-8">
<title>tendly — Dashboard</title>
<link href="https://fonts.googleapis.com/css2?family=Nunito+Sans:wght@400;600;700&display=swap" rel="stylesheet">
<style>
  :root{
    --page:#f2f2f2;
    --teal:#62cad4;
    --teal-dark:#55bfca;
    --ink:#1c1c1c;
    --muted:#555b63;
    --soft:#a9adb3;
    --line:#e6e8ea;
    --sidebar:#f9f9f9;
    --white:#ffffff;
    --black:#000000;
    --green:#3cc47c;
    --red:#e35d5d;
    --blue:#3aa0e8;
    --gray-dot:#9a9a9a;
    --brand-gray:#a7a7a7;
  }
  *{box-sizing:border-box;margin:0;padding:0}
  html,body{width:1200px;height:1047px;overflow:hidden}
  body{background:var(--page);font-family:"Nunito Sans",Arial,sans-serif;color:var(--ink);position:relative}
  .abs{position:absolute}

  .brand-title{left:0;top:74px;width:1200px;text-align:center;font-size:30px;font-weight:700;color:var(--brand-gray);letter-spacing:.3px}

  .app{left:47px;top:160px;width:1108px;height:788px;background:var(--page);box-shadow:0 20px 50px rgba(0,0,0,.06)}
  .sidebar{left:0;top:0;width:283px;height:788px;background:var(--sidebar)}
  .sidebar-head{left:0;top:0;width:283px;height:55px;background:var(--teal);overflow:hidden}
  .sidebar-head .name{left:18px;top:14px;font-size:19px;font-weight:700;color:var(--white)}
  .menu-toggle{left:239px;top:-8px;width:70px;height:70px;border-radius:50%;background:var(--teal-dark)}
  .menu-toggle svg{position:absolute;left:15px;top:35px}

  .new-ticket{left:24px;top:86px;width:234px;height:43px;background:var(--white);border:1px solid var(--line);border-radius:3px}
  .new-ticket .plus{left:12px;top:12px;width:19px;height:19px;border:1px solid var(--teal);border-radius:2px;color:var(--teal);font-size:11px;text-align:center;line-height:17px;background:#eefafb}
  .new-ticket .label{left:42px;top:12px;font-size:11.5px;font-weight:600}
  .new-ticket .more{left:216px;top:13px}

  .nav{list-style:none}
  .nav li{position:absolute;left:42px;display:flex;align-items:center;gap:12px;font-size:11px;font-weight:600;letter-spacing:.1px}
  .nav li.active{color:var(--teal)}

  .topbar{left:283px;top:0;width:825px;height:55px;background:var(--black);color:var(--white)}
  .greeting{left:18px;top:17px;font-size:14.5px;font-weight:700}
  .greeting span{color:var(--teal)}
  .search{left:582px;top:14px;width:153px;height:27px;border:1px solid #4a4a4a;border-radius:14px;font-size:8px;font-weight:700;padding:7px 0 0 14px}
  .search svg{position:absolute;right:12px;top:6px}
  .avatar{left:759px;top:14px;width:27px;height:27px;border-radius:50%;background:linear-gradient(135deg,#8a6d5c,#3b2d27)}
  .chevron{left:793px;top:24px}

  .stats{left:283px;top:55px;width:825px;height:167px;background:var(--teal)}
  .stat{position:absolute;top:30px;width:120px;text-align:center;transform:translateX(-50%)}
  .stat .num{font-size:37px;font-weight:600;color:var(--white);line-height:1}
  .stat .lab{font-size:11px;font-weight:600;margin-top:10px}
  .divider{position:absolute;top:0;width:1px;height:123px;background:rgba(255,255,255,.25)}

  .card{left:310px;top:179px;width:780px;height:547px;background:var(--white);border-radius:8px}
  .card-title{left:62px;top:36px;font-size:9.5px;font-weight:700;letter-spacing:.2px}
  .rail{left:71px;top:66px;width:3px;height:418px;background:#ececec}
  .dot{position:absolute;width:12px;height:12px;border-radius:50%;background:var(--white);border:1.5px solid}
  .day{position:absolute;left:128px;font-size:12.5px;font-weight:700;color:#3a3f46}
  .row{position:absolute;left:94px;width:412px;font-size:10px;color:var(--muted)}
  .row .time{position:absolute;left:0;top:1px;font-size:8.5px;color:var(--soft)}
  .row .text{position:absolute;left:37px;line-height:18px;white-space:nowrap}
  .rule{position:absolute;left:94px;width:412px;height:1px;background:var(--line)}
  .faded{opacity:.45}
</style>
</head>
<body>
  <div class="abs brand-title">tendly</div>

  <div class="abs app">
    <aside class="abs sidebar">
      <div class="abs sidebar-head">
        <div class="abs name">tendly</div>
        <div class="abs menu-toggle">
          <svg width="16" height="12" viewBox="0 0 16 12"><g stroke="#fff" stroke-width="1.6"><line x1="0" y1="1" x2="16" y2="1"/><line x1="0" y1="6" x2="16" y2="6"/><line x1="0" y1="11" x2="16" y2="11"/></g></svg>
        </div>
      </div>

      <div class="abs new-ticket">
        <div class="abs plus">+</div>
        <div class="abs label">New Ticket</div>
        <svg class="abs more" width="4" height="16" viewBox="0 0 4 16"><g fill="#c5c8cc"><circle cx="2" cy="2" r="1.5"/><circle cx="2" cy="8" r="1.5"/><circle cx="2" cy="14" r="1.5"/></g></svg>
      </div>

      <ul class="nav">
        <li class="active" style="top:165px">
          <svg width="13" height="13" viewBox="0 0 14 14" fill="none" stroke="#62cad4"><circle cx="7" cy="7" r="6"/><circle cx="7" cy="7" r="3"/></svg>DASHBOARD</li>
        <li style="top:209px">
          <svg width="13" height="13" viewBox="0 0 14 14" fill="none" stroke="#1c1c1c"><path d="M1 3.5h9l3 3.5-3 3.5H1z"/></svg>TICKETS</li>
        <li style="top:251px">
          <svg width="13" height="13" viewBox="0 0 14 14" fill="none" stroke="#1c1c1c"><circle cx="7" cy="4" r="3"/><path d="M1.5 13c0-3 2.5-5 5.5-5s5.5 2 5.5 5z"/></svg>CONTACTS</li>
        <li style="top:295px">
          <svg width="13" height="13" viewBox="0 0 14 14" fill="none" stroke="#1c1c1c"><circle cx="7" cy="7" r="2.2"/><circle cx="7" cy="7" r="5.4" stroke-dasharray="2.4 1.8"/></svg>ADMIN SETTINGS</li>
        <li style="top:338px">
          <svg width="14" height="13" viewBox="0 0 15 14" fill="none" stroke="#1c1c1c"><rect x="1" y="7" width="3" height="6"/><rect x="6" y="2" width="3" height="11"/><rect x="11" y="5" width="3" height="8"/></svg>ACCOUNT &amp; BILLING</li>
      </ul>
    </aside>

    <header class="abs topbar">
      <div class="abs greeting">Good Morning, <span>Marcus</span></div>
      <div class="abs search">Search for tickets
        <svg width="14" height="14" viewBox="0 0 14 14" fill="none" stroke="#62cad4" stroke-width="1.8"><circle cx="5.5" cy="5.5" r="4.3"/><line x1="8.8" y1="8.8" x2="13" y2="13"/></svg>
      </div>
      <div class="abs avatar" role="img" aria-label="User profile photo"></div>
      <svg class="abs chevron" width="10" height="6" viewBox="0 0 10 6" fill="none" stroke="#62cad4" stroke-width="1.3"><path d="M1 1l4 4 4-4"/></svg>
    </header>

    <section class="abs stats">
      <div class="stat" style="left:77px"><div class="num">150</div><div class="lab">Open Tickets</div></div>
      <div class="divider" style="left:133px"></div>
      <div class="stat" style="left:187px"><div class="num">23</div><div class="lab">Due Today</div></div>
      <div class="divider" style="left:245px"></div>
      <div class="stat" style="left:292px"><div class="num">14</div><div class="lab">Unassigned</div></div>
      <div class="divider" style="left:356px"></div>
      <div class="stat" style="left:409px"><div class="num">34</div><div class="lab">Over Due</div></div>
      <div class="divider" style="left:467px"></div>
      <div class="stat" style="left:532px"><div class="num">60</div><div class="lab">On Hold</div></div>
      <div class="divider" style="left:602px"></div>
      <div class="stat" style="left:667px"><div class="num">11</div><div class="lab">Not Resolved</div></div>
    </section>

    <section class="abs card">
      <div class="abs card-title">RECENT ACTIVITIES</div>
      <div class="abs rail"></div>
      <div class="dot" style="left:67px;top:62px;width:9px;height:9px;background:var(--gray-dot);border:none"></div>

      <div class="dot" style="left:66px;top:98px;border-color:var(--green)"></div>
      <div class="day" style="top:96px">Today</div>
      <div class="row" style="top:123px"><span class="time">5pm</span><span class="text" style="left:40px">Lena Ortiz assigned forgot to cc, trying again (#15) to Lena Ortiz.</span></div>
      <div class="rule" style="top:143px"></div>
      <div class="row" style="top:158px"><span class="time">5pm</span><span class="text" style="left:40px">Lena Ortiz assigned forgot to cc,</span></div>

      <div class="dot" style="left:66px;top:215px;border-color:var(--red)"></div>
      <div class="day" style="top:213px">Yesterday</div>
      <div class="row" style="top:247px"><span class="time">3-4pm</span><span class="text">Lena Ortiz assigned forgot to cc.</span></div>
      <div class="rule" style="top:268px"></div>
      <div class="row" style="top:281px"><span class="time">3-4pm</span><span class="text">Lena Ortiz assigned forgot to cc, trying again (#15) to Lena Ortiz.</span></div>
      <div class="rule" style="top:303px"></div>
      <div class="row" style="top:319px"><span class="time">3-4pm</span><span class="text">Lena Ortiz assigned forgot to cc,</span></div>

      <div class="dot" style="left:66px;top:381px;border-color:var(--blue)"></div>
      <div class="row" style="top:381px"><span class="time">10pm</span><span class="text">Skyglass space telescope probably ranks next to the moon landings<br>and the development…</span></div>

      <div class="dot" style="left:66px;top:470px;border-color:var(--gray-dot)"></div>
      <div class="row faded" style="top:470px"><span class="time">9pm</span><span class="text">While Orbitra has had many ups and downs, the launch and</span></div>
    </section>
  </div>
</body>
</html>
```